Voltrix GmbH needs a sensational homepage!

A draft of the performances and the logo were uploaded in the attachment. The homepage should be adapted to the colors of the logo. Either pictures, graphics or icons of the respective topic are to be used for the buttons. Social media Linkedin, Youtube, Instagram should not be missing. An imprint, contact form with telephone number and email address should be given on the home page. The page should definitely be designed to be responsive for all end devices. Texts as well as images and videos are inserted in the sub-menus or pages. Only the structure and a simple application should be given. We have already secured the domain www.voltrix.at.
We are a young, dynamic company with a high technical affinity. Ask for creative suggestions. If something is needed, please contact us.

Target Market(s)

Construction industry, client

Requirements
Must have
• see description
Should not have
• shouldn't be colorful and playful

```html
<!DOCTYPE html>
<html lang="de">
<head>
<meta charset="utf-8">
<title>Voltrix GmbH</title>
<link href="https://fonts.googleapis.com/css2?family=Lato:wght@400;700&family=Raleway:wght@500;600&display=swap" rel="stylesheet">
<style>
:root{
  --teal:#2f4a53;
  --teal-dark:#263d45;
  --white:#ffffff;
  --text:#2b2b2b;
  --muted:#6b7376;
  --rule:#e4e6e7;
}
*{margin:0;padding:0;box-sizing:border-box}
html,body{width:1200px;height:1037px;overflow:hidden;background:var(--white)}
body{position:relative;font-family:'Lato',sans-serif;color:var(--text)}
.hero{position:absolute;left:0;top:0;width:1200px;height:681px;
  background:linear-gradient(180deg,#2c3d43 0%,#4d6068 35%,#7d8d93 70%,#9aa7ab 100%)}
.topbar{position:absolute;top:24px;left:100px;right:100px;display:flex;justify-content:space-between;align-items:center;color:var(--white)}
.social{display:flex;align-items:center;gap:0;list-style:none}
.social li{display:flex;align-items:center}
.social li+li::before{content:"";width:1px;height:10px;background:rgba(255,255,255,.5);margin:0 14px}
.social .dot{width:12px;height:12px;border-radius:50%;background:var(--white);display:block}
.contact{display:flex;align-items:center;font-size:13.5px;font-weight:700}
.contact span{display:flex;align-items:center;gap:8px}
.contact .sep{width:1px;height:10px;background:rgba(255,255,255,.5);margin:0 20px}
.brand{position:absolute;top:270px;left:0;width:1200px;text-align:center;color:var(--white);
  font-family:'Lato',sans-serif;font-weight:400;font-size:72px;letter-spacing:14px}
.card{position:absolute;background:var(--white);box-shadow:0 4px 18px rgba(0,0,0,.08)}
.card-left{left:100px;top:604px;width:334px;height:293px}
.card-right{left:767px;top:604px;width:334px;height:293px}
.card-mid{left:434px;top:561px;width:333px;height:379px;background:var(--teal);color:var(--white);box-shadow:0 6px 22px rgba(0,0,0,.15)}
.card-head{position:absolute;left:34px;top:26px;display:flex;align-items:center;gap:26px}
.card-title{font-family:'Raleway',sans-serif;font-weight:600;font-size:19px;color:var(--teal);line-height:29px}
.card-mid .card-title{color:var(--white)}
.card-list{position:absolute;left:34px;list-style:none;font-size:14px}
.card-list li{position:relative;padding-left:24px;height:30.2px;line-height:20px}
.card-list li::before{content:"";position:absolute;left:0;top:6px;width:7px;height:7px;border-radius:50%;background:var(--teal)}
.card-mid .card-list li::before{background:var(--white)}
.btn{position:absolute;display:flex;align-items:center;justify-content:center;gap:16px;
  font-family:'Raleway',sans-serif;font-weight:600;font-size:15.5px;letter-spacing:.5px;color:var(--teal);
  border:1px solid var(--teal);height:38px;width:154px;background:var(--white)}
.card-left .btn,.card-right .btn{left:95px;top:235px}
.card-mid .btn{left:90px;top:293px;border-color:var(--white);height:37px;width:152px}
.footer-rule{position:absolute;left:100px;right:98px;top:991px;height:1px;background:var(--rule)}
.copyright{position:absolute;top:1007px;width:1200px;text-align:center;font-family:'Raleway',sans-serif;font-size:12px;color:var(--muted)}
</style>
</head>
<body>
<div class="hero" role="img" aria-label="Foto eines eingerüsteten Hochhauses mit Baukran vor bewölktem Himmel"></div>

<header class="topbar">
  <ul class="social" aria-label="Soziale Netzwerke">
    <li><span class="dot"></span></li>
    <li><span class="dot"></span></li>
    <li><span class="dot"></span></li>
  </ul>
  <div class="contact">
    <span>
      <svg width="16" height="16" viewBox="0 0 24 24" fill="none" stroke="#fff" stroke-width="1.8" stroke-linejoin="round"><path d="M5 3h4l2 5-2.5 1.5a11 11 0 0 0 6 6L16 13l5 2v4a2 2 0 0 1-2 2A16 16 0 0 1 3 5a2 2 0 0 1 2-2z"/></svg>
      (555)-014-2290
    </span>
    <i class="sep"></i>
    <span>
      <svg width="17" height="14" viewBox="0 0 24 18" fill="none" stroke="#fff" stroke-width="1.8"><rect x="1" y="1" width="22" height="16"/><path d="M1 1l11 9 11-9"/></svg>
      info@voltrix.at
    </span>
  </div>
</header>

<div class="brand">VOLTRIX GmbH</div>

<section class="card card-left">
  <div class="card-head">
    <svg width="42" height="42" viewBox="0 0 42 42" fill="none" stroke="#2f4a53" stroke-width="2"><path d="M4 2v40M38 2v40M4 6h34M4 20h34M4 36h34M4 20l34 16M38 20L4 36M4 6l34 14M38 6L4 20"/></svg>
    <h2 class="card-title">Gerüstbau</h2>
  </div>
  <ul class="card-list" style="top:106px">
    <li>Gerüstbau</li>
    <li>Gerüstverleih</li>
    <li>Aufbauanleitung</li>
  </ul>
  <a class="btn">ANFRAGE
    <svg width="18" height="12" viewBox="0 0 18 12" fill="none" stroke="#2f4a53" stroke-width="1.8"><path d="M0 6h16M11 1l5 5-5 5"/></svg></a>
</section>

<section class="card card-mid">
  <div class="card-head" style="top:44px;gap:22px;align-items:flex-start">
    <svg width="42" height="42" viewBox="0 0 42 42" fill="none" stroke="#fff" stroke-width="2"><path d="M4 2v36M10 2v36M22 2v36M28 2v36M2 38h38M2 42h38M28 30h6v8M28 24h4"/></svg>
    <h2 class="card-title" style="margin-top:-8px">Sanierung<br>Projektmanagement</h2>
  </div>
  <ul class="card-list" style="top:149px">
    <li>Betoninstandsetzung</li>
    <li>Bauwerksabdichtung</li>
    <li>Fassadensanierung</li>
    <li>Alu,Kunststoff,Holzfenster</li>
  </ul>
  <a class="btn">ANFRAGE
    <svg width="18" height="12" viewBox="0 0 18 12" fill="none" stroke="#2f4a53" stroke-width="1.8"><path d="M0 6h16M11 1l5 5-5 5"/></svg></a>
</section>

<section class="card card-right">
  <div class="card-head" style="top:24px;gap:16px">
    <svg width="48" height="36" viewBox="0 0 48 36" fill="none" stroke="#2f4a53" stroke-width="1.6"><circle cx="17" cy="17" r="16"/><circle cx="17" cy="17" r="9"/><circle cx="17" cy="17" r="4"/><path d="M17 33h30v-8h-8"/></svg>
    <h2 class="card-title">Estrich &amp; Isolierung</h2>
  </div>
  <ul class="card-list" style="top:106px">
    <li>Roboter</li>
    <li>Silotechnik</li>
    <li>Dämmung</li>
    <li>Videos</li>
  </ul>
  <a class="btn">ANFRAGE
    <svg width="18" height="12" viewBox="0 0 18 12" fill="none" stroke="#2f4a53" stroke-width="1.8"><path d="M0 6h16M11 1l5 5-5 5"/></svg></a>
</section>

<div class="footer-rule"></div>
<footer class="copyright">© 2021 Voltrix GmbH.</footer>
</body>
</html>
```